Real Estate Company
Tolin Estate Partners
Project: Real Estate Company
Real Estate Company - Real Estate
Creative Brief
Professional
Dale Moxon
Broker
PO Box 3152 Fresno, CA 93729
dale@tolinestatepartners.com
www.tolinestatepartners.com
BRE # 04527391
Card should have rounded edges.
one side of card should have all the info and one side should have logo + website

```html
<!DOCTYPE html>
<html lang="en">
<head>
<meta charset="utf-8">
<title>Tolin Estate Partners – Business Cards</title>
<link rel="stylesheet" href="https://fonts.googleapis.com/css2?family=Open+Sans:wght@400;600;700&display=swap">
<style>
  :root {
    --backdrop: #e8e4df;
    --card: #ffffff;
    --brand-blue: #1f73b7;
    --brand-blue-light: #3fa3e4;
    --brand-blue-dark: #0f4f8c;
    --rule-grey: #b9bcc0;
    --ink: #2f3236;
    --ink-soft: #55595e;
    --shadow: rgba(40, 30, 20, 0.28);
  }
  * { box-sizing: border-box; margin: 0; padding: 0; }
  html, body { width: 1200px; height: 912px; overflow: hidden; }
  body {
    background: var(--backdrop);
    font-family: "Open Sans", Arial, sans-serif;
    position: relative;
  }
  .card {
    position: absolute;
    width: 560px;
    height: 320px;
    background: var(--card);
    border-radius: 28px;
    overflow: hidden;
    box-shadow: 0 18px 40px var(--shadow);
  }
  .card--logo { left: 70px; top: 110px; }
  .card--info { left: 570px; top: 480px; }

  .brand {
    display: flex;
    align-items: center;
    gap: 14px;
    color: var(--brand-blue);
    font-weight: 600;
    letter-spacing: 0.04em;
  }
  .brand__mark {
    width: 30px; height: 30px;
    background: var(--brand-blue);
    flex: none;
  }
  .front-lockup {
    position: absolute;
    inset: 0;
    display: flex;
    flex-direction: column;
    align-items: center;
    justify-content: center;
    gap: 14px;
  }
  .front-lockup .brand { font-size: 28px; }
  .front-lockup__web {
    font-size: 13px;
    letter-spacing: 0.08em;
    color: var(--ink-soft);
  }
  .card--info .brand {
    position: absolute;
    right: 34px; top: 36px;
    font-size: 15px;
    gap: 10px;
  }
  .card--info .brand__mark { width: 22px; height: 22px; }

  .swoosh { position: absolute; inset: 0; width: 100%; height: 100%; }

  .contact {
    position: absolute;
    left: 34px; top: 76px;
    color: var(--ink);
  }
  .contact__name { font-size: 17px; font-weight: 700; line-height: 22px; }
  .contact__role { font-size: 14px; line-height: 19px; color: var(--ink-soft); margin-bottom: 10px; }
  .contact__line {
    display: flex; align-items: center; gap: 7px;
    font-size: 11.5px; line-height: 17px; color: var(--ink-soft);
  }
  .contact__icon { width: 11px; height: 11px; flex: none; }
  .contact__spacer { width: 11px; flex: none; }
</style>
</head>
<body>

  <section class="card card--logo" aria-label="Card front">
    <div class="front-lockup">
      <div class="brand"><span class="brand__mark"></span><span>Tolin Estate Partners</span></div>
      <p class="front-lockup__web">www.tolinestatepartners.com</p>
    </div>
  </section>

  <section class="card card--info" aria-label="Card back">
    <svg class="swoosh" viewBox="0 0 560 320" preserveAspectRatio="none" aria-hidden="true">
      <defs>
        <linearGradient id="bandBlue" x1="0" y1="0" x2="1" y2="1">
          <stop offset="0" stop-color="var(--brand-blue-light)"/>
          <stop offset="0.55" stop-color="var(--brand-blue)"/>
          <stop offset="1" stop-color="var(--brand-blue-dark)"/>
        </linearGradient>
      </defs>
      <path d="M0 292 C 220 300, 420 250, 560 118 L560 320 L0 320 Z" fill="url(#bandBlue)"/>
      <path d="M0 279 C 220 288, 420 236, 560 104" fill="none" stroke="var(--rule-grey)" stroke-width="5"/>
    </svg>

    <div class="brand"><span class="brand__mark"></span><span>Tolin Estate Partners</span></div>

    <div class="contact">
      <p class="contact__name">Dale Moxon</p>
      <p class="contact__role">Broker</p>
      <p class="contact__line"><span class="contact__spacer"></span>PO Box 3152</p>
      <p class="contact__line"><span class="contact__spacer"></span>Fresno, CA 93729</p>
      <p class="contact__line">
        <svg class="contact__icon" viewBox="0 0 12 12" aria-hidden="true"><path d="M2 1h3l1 3-1.5 1a6 6 0 0 0 2.5 2.5L8 6l3 1v3a1 1 0 0 1-1 1A9 9 0 0 1 1 2a1 1 0 0 1 1-1z" fill="var(--ink-soft)"/></svg>
        (559) 555-0148
      </p>
      <p class="contact__line">
        <svg class="contact__icon" viewBox="0 0 12 12" aria-hidden="true"><rect x="1" y="2" width="10" height="8" rx="1" fill="var(--ink-soft)"/></svg>
        BRE # 04527391
      </p>
      <p class="contact__line">
        <svg class="contact__icon" viewBox="0 0 12 12" aria-hidden="true"><rect x="1" y="2.5" width="10" height="7" rx="1" fill="none" stroke="var(--ink-soft)" stroke-width="1.2"/><path d="M1.5 3l4.5 3.5L10.5 3" fill="none" stroke="var(--ink-soft)" stroke-width="1.2"/></svg>
        dale@tolinestatepartners.com
      </p>
      <p class="contact__line">
        <svg class="contact__icon" viewBox="0 0 12 12" aria-hidden="true"><circle cx="6" cy="6" r="4.8" fill="none" stroke="var(--ink-soft)" stroke-width="1.2"/><path d="M1.2 6h9.6M6 1.2c2 2.4 2 7.2 0 9.6M6 1.2c-2 2.4-2 7.2 0 9.6" fill="none" stroke="var(--ink-soft)" stroke-width="0.9"/></svg>
        www.tolinestatepartners.com
      </p>
    </div>
  </section>

</body>
</html>
```